Sports Betting Business Consultant

After 21 years in corporate life. Will be continue as consultant/advisor in sports betting industry. Need a business card. Prefer an iphone format as layout. Elements; betting,ticket, sports types soccer, basketball, tennis etc , odds etc.

```html
<!DOCTYPE html>
<html lang="en">
<head>
<meta charset="UTF-8">
<title>Deniz Karan – Sports Advisor Business Card</title>
<link href="https://fonts.googleapis.com/css2?family=Lato:wght@400;900&display=swap" rel="stylesheet">
<style>
  :root {
    --stage: #3a3b3f;
    --card-dark: #1d1d21;
    --card-light: #ffffff;
    --ink: #141414;
    --ink-soft: #3a3a3a;
    --figure-grey: #6e6b69;
    --figure-black: #111111;
  }
  * { margin: 0; padding: 0; box-sizing: border-box; }
  html, body {
    width: 1200px;
    height: 900px;
    overflow: hidden;
  }
  body {
    background: var(--stage);
    font-family: "Lato", sans-serif;
    display: flex;
    flex-direction: column;
    align-items: center;
    justify-content: center;
    gap: 50px;
  }
  .card {
    position: relative;
    width: 600px;
    height: 340px;
    border-radius: 26px;
    overflow: hidden;
  }
  .card--back { background: var(--card-dark); }
  .card--front { background: var(--card-light); }

  .athletes {
    position: absolute;
    border-radius: 40px;
  }
  .card--back .athletes {
    left: 170px;
    top: 50px;
    width: 260px;
    height: 240px;
    background: radial-gradient(ellipse at center, var(--figure-grey) 0%, rgba(110,107,105,0.55) 60%, rgba(110,107,105,0) 100%);
  }
  .card--front .athletes {
    right: 36px;
    top: 36px;
    width: 230px;
    height: 220px;
    background: radial-gradient(ellipse at center, var(--figure-black) 0%, rgba(17,17,17,0.6) 60%, rgba(17,17,17,0) 100%);
  }

  .accent-bar {
    position: absolute;
    left: 0;
    top: 118px;
    width: 22px;
    height: 46px;
    background: var(--ink);
  }
  .identity {
    position: absolute;
    left: 58px;
    top: 88px;
    width: 300px;
    color: var(--ink);
  }
  .identity__name {
    font-weight: 900;
    font-size: 32px;
    letter-spacing: 0.5px;
    line-height: 1;
  }
  .identity__role {
    font-size: 18px;
    line-height: 1.2;
    color: var(--ink-soft);
    margin-top: 6px;
  }
  .contact {
    list-style: none;
    margin-top: 18px;
    font-size: 18px;
    line-height: 1.2;
    color: var(--ink-soft);
  }
  .contact__item {
    display: flex;
    align-items: center;
    gap: 14px;
    margin-bottom: 6px;
  }
  .contact__icon { width: 20px; height: 20px; flex: none; }
  .services {
    margin-top: 12px;
    font-size: 18px;
    line-height: 1.25;
    color: var(--ink-soft);
  }
</style>
</head>
<body>

  <section class="card card--back" aria-label="Card back">
    <div class="athletes" role="img" aria-label="Grey silhouettes of athletes playing soccer, tennis and volleyball"></div>
  </section>

  <section class="card card--front" aria-label="Card front">
    <span class="accent-bar"></span>
    <div class="identity">
      <h1 class="identity__name">DENIZ KARAN</h1>
      <p class="identity__role">Sports Advisor</p>
      <ul class="contact">
        <li class="contact__item">
          <svg class="contact__icon" viewBox="0 0 24 24" aria-hidden="true">
            <path fill="#141414" d="M6.6 10.8a15.1 15.1 0 0 0 6.6 6.6l2.2-2.2c.3-.3.7-.4 1-.2 1.1.4 2.3.6 3.6.6.6 0 1 .4 1 1V20c0 .6-.4 1-1 1A17 17 0 0 1 3 4c0-.6.4-1 1-1h3.5c.6 0 1 .4 1 1 0 1.3.2 2.5.6 3.6.1.3 0 .7-.2 1z"/>
          </svg>
          <span>+90 555 014 2217</span>
        </li>
        <li class="contact__item">
          <svg class="contact__icon" viewBox="0 0 24 24" aria-hidden="true">
            <rect x="2" y="5" width="20" height="14" fill="#141414"/>
            <path d="M2 5l10 8 10-8" fill="none" stroke="#fff" stroke-width="1.6"/>
          </svg>
          <span>dnzkrn@postmail.com</span>
        </li>
      </ul>
      <p class="services">Betting, Ticket, Soccer,<br>Basketball, Tennis Etc</p>
    </div>
    <div class="athletes" role="img" aria-label="Black silhouettes of athletes playing soccer, tennis and volleyball"></div>
  </section>

</body>
</html>
```